Automotive Repair Centre - Flyer Design

Bremwick Motors Cumbernauld are looking for a completely new flyer design for our blossoming auto repair centre. We are looking for bold eye catching designs as these flyers will be letterbox dropped around the local community. Approx. 10k per month. These will be printed double sided, on A5, with different print front and rear. Currently the whole rear is dedicated to servicing only, but this can be changed.

Our business prides itself on providing a high quality service so they flyer needs to convey this message. Also we believe in fair prices so they flyer also needs to convey this message in the design. Colour scheme is currently blue, yellow, and black. If possible it would be good to include the Drivemarq logo and the KELP logo.

We like the "specials" list from the Halvorn Drake flyer that is attached. We also like the clean look and layout of the other flyer that is uploaded. It would be good to include a special area for winter tyres much like is shown in the 50% off wheel alignment piece of the flyer attached.

Our current flyer uses the font GoodTimes as we would like this to remain if possible. It can be changed if the designer prefers. You can visit our website www.bremwick.co.uk for more information about our business.
Updates

Reason: Not had enough good designs to choose from yet.

Reason: Still not enough good designs to choose from

Reason: designs not up to the standard required.

Reason: Not enough designs that capture the brief have been submitted

Reason: looking for more designs

Reason: looking for some more bright designs. please read the brief!!!

Reason: same as before

Target Market(s)

General public.

Industry/Entity Type

Wheel

Requirements
Should not have
• We feel the flyer should not have photos of high end vehicles like Zantellis etc as the does not fit our approach of good value.

```html
<!DOCTYPE html>
<html lang="en">
<head>
<meta charset="utf-8">
<title>Bremwick Motors – Flyers</title>
<link rel="stylesheet" href="https://fonts.googleapis.com/css2?family=Michroma&family=Open+Sans:wght@400;600&display=swap">
<style>
  :root {
    --bg: #1d1d1f;
    --paper: #ffffff;
    --brand-blue: #0a72bb;
    --brand-yellow: #f5ee1c;
    --ink: #111111;
    --rule: #333333;
  }
  * { box-sizing: border-box; margin: 0; padding: 0; }
  html, body { width: 1200px; height: 793px; overflow: hidden; background: var(--bg); }
  body { position: relative; font-family: "Open Sans", Arial, sans-serif; }

  .flyer { position: absolute; top: 80px; width: 445px; height: 628px; background: var(--paper); overflow: hidden; }
  .flyer--front { left: 92px; }
  .flyer--back { left: 669px; width: 444px; }

  .brand-header {
    position: absolute; left: 22px; top: 18px; width: 396px; height: 168px;
    background: var(--brand-blue); border-radius: 12px;
    display: flex; align-items: center; justify-content: center; gap: 16px;
  }
  .brand-header__dot { width: 34px; height: 34px; border-radius: 50%; background: var(--brand-yellow); }
  .brand-header__name { font-family: "Michroma", sans-serif; color: #fff; font-size: 34px; letter-spacing: 1px; }

  .photo { position: absolute; border-radius: 8px; }
  .photo--mot { left: 22px; top: 198px; width: 93px; height: 92px; background: linear-gradient(135deg, #cfd4d8, #5c6a78 70%, #2d3e55); }
  .photo--wheel { left: 22px; top: 314px; width: 93px; height: 146px; background: linear-gradient(160deg, #e8eaec, #8e959c 55%, #2f4f86); }

  .offer { position: absolute; left: 126px; top: 224px; font-family: "Michroma", sans-serif; white-space: nowrap; }
  .offer__title { color: var(--brand-blue); font-size: 19px; line-height: 1.2; }
  .offer__price { color: var(--ink); font-size: 32px; line-height: 1.15; }

  .rule { position: absolute; left: 22px; width: 396px; height: 1.5px; background: var(--rule); }
  .rule--top { top: 299px; }
  .rule--bottom { top: 470px; }

  .service-list { position: absolute; left: 126px; top: 320px; list-style: none; font-family: "Michroma", sans-serif; font-size: 18px; color: var(--ink); }
  .service-list li { height: 37.7px; }

  .also-box {
    position: absolute; left: 22px; top: 482px; width: 93px; height: 66px;
    background: var(--brand-blue); border-radius: 7px; padding: 8px 4px;
    font-family: "Michroma", sans-serif; font-size: 12.5px; line-height: 1.2; color: var(--brand-yellow);
  }
  .also-list { position: absolute; left: 126px; top: 494px; list-style: none; font-family: "Michroma", sans-serif; font-size: 6.8px; color: var(--brand-blue); white-space: nowrap; }
  .also-list li { height: 17px; }

  .contact-band {
    position: absolute; left: 22px; top: 568px; width: 300px; height: 45px;
    border-radius: 8px 0 0 8px; padding: 5px 12px;
    background: linear-gradient(90deg, var(--brand-blue) 70%, rgba(10,114,187,0));
    color: #fff; font-size: 8.6px; line-height: 1.45; white-space: nowrap;
  }

  .mascot { position: absolute; border-radius: 45% 45% 10px 10px; background: linear-gradient(180deg, #f0c9a4 0%, #e3833a 12%, #2f5fa3 35%, #1f3f75 70%, #6f7378 100%); }
  .flyer--front .mascot { left: 294px; top: 432px; width: 151px; height: 196px; }
  .flyer--back .mascot { left: 288px; top: 432px; width: 150px; height: 196px; }

  .servicing-panel { position: absolute; left: 22px; top: 199px; width: 394px; height: 200px; background: var(--brand-yellow); font-family: "Michroma", sans-serif; white-space: nowrap; }
  .servicing-panel__title { position: absolute; left: 22px; top: 10px; font-size: 43px; color: var(--brand-blue); }
  .servicing-panel__price { position: absolute; right: 18px; top: 64px; font-size: 32px; color: var(--ink); }
  .servicing-panel__items { position: absolute; left: 0; right: 0; top: 128px; text-align: center; font-size: 11.5px; line-height: 1.45; color: var(--brand-blue); }
  .servicing-panel__items span { margin: 0 5px; }
  .servicing-panel__note { position: absolute; right: 10px; bottom: 8px; font-family: "Open Sans", sans-serif; font-size: 8px; color: var(--ink); }

  .parts-callout {
    position: absolute; left: 22px; top: 412px; width: 247px; height: 88px;
    border: 1.3px dashed var(--brand-blue); border-radius: 10px; padding: 10px 12px;
  }
  .parts-callout__tail { position: absolute; left: 268px; top: 420px; z-index: 2; }
  .parts-callout__title { font-family: "Michroma", sans-serif; color: var(--brand-blue); font-size: 10.5px; margin-bottom: 8px; white-space: nowrap; }
  .parts-callout__text { font-size: 7.4px; line-height: 1.5; color: var(--ink); white-space: nowrap; }

  .tagline { position: absolute; left: 61px; top: 531px; font-family: "Michroma", sans-serif; font-size: 7px; color: var(--ink); white-space: nowrap; }
</style>
</head>
<body>

<section class="flyer flyer--front">
  <header class="brand-header"><span class="brand-header__dot"></span><span class="brand-header__name">BREMWICK</span></header>

  <div class="photo photo--mot" role="img" aria-label="Photo of a mechanic working on a raised car wheel"></div>
  <div class="offer">
    <p class="offer__title">MOT TESTING</p>
    <p class="offer__price">ONLY £35</p>
  </div>
  <div class="rule rule--top"></div>

  <div class="photo photo--wheel" role="img" aria-label="Close-up photo of a car wheel and tyre"></div>
  <ul class="service-list">
    <li>TYRES</li><li>BRAKES</li><li>EXHAUSTS</li><li>CLUTCHES</li>
  </ul>
  <div class="rule rule--bottom"></div>

  <div class="also-box">WE<br>ALSO<br>PROVIDE</div>
  <ul class="also-list">
    <li>FAULT DIAGNOSTICS</li>
    <li>BATTERIES WHEEL ALIGNMENT</li>
    <li>WELDING AND MORE</li>
  </ul>

  <div class="contact-band">
    14-16 Corran Lane, Westfield Trading Park<br>
    Cumbernauld, G68 4QT<br>
    Tel: 01236 418204, Email: sales@bremwick.co.uk
  </div>
  <div class="mascot" role="img" aria-label="Illustrated mechanic holding a spanner and a wheel"></div>
</section>

<section class="flyer flyer--back">
  <header class="brand-header"><span class="brand-header__dot"></span><span class="brand-header__name">BREMWICK</span></header>

  <div class="servicing-panel">
    <p class="servicing-panel__title">SERVICING</p>
    <p class="servicing-panel__price">ONLY £85</p>
    <p class="servicing-panel__items">
      <span>·SPARK PLUGS</span><span>·OIL FILTER</span><span>·LONG LIFE OIL</span><br>
      <span>·AIR FILTER</span><span>·VEHICLE SAFETY CHECK</span>
    </p>
    <p class="servicing-panel__note">ENY VEHICLE UP TO 2000cc</p>
  </div>

  <div class="parts-callout">
    <p class="parts-callout__title">WHAT PARTS DO WE USE?</p>
    <p class="parts-callout__text">
      We Use Only High Quality Oem Equivalent Parts.<br>
      We Use Vantor Or Kessling Spark Plugs. High Quality Filters<br>
      And Premium Long Life Oil.
    </p>
  </div>
  <svg class="parts-callout__tail" width="24" height="32" viewBox="0 0 24 32" aria-hidden="true">
    <path d="M1 14 L22 30 M1 26 L14 22" stroke="#0a72bb" stroke-width="1.3" stroke-dasharray="3 2" fill="none"/>
  </svg>

  <p class="tagline">EXPERT ADVICE IN PLAIN ENGLISH</p>

  <div class="contact-band">
    14-16 Corran Lane, Westfield Trading Park<br>
    Cumbernauld, G68 4QT<br>
    Tel: 01236 418204, Email: sales@bremwick.co.uk
  </div>
  <div class="mascot" role="img" aria-label="Illustrated mechanic holding a spanner and a wheel"></div>
</section>

</body>
</html>
```